Business Card for beauty technology startup

Design Glowmi Business Card for a Beauty, based on the website identity and colors (https://www.glowmi-example.com).
Glowmi is a beauty tech startup that gathers helpful product info for beauty lovers and consumers (such as availability on stores, price range and product reviews) for makeup products. The card design must be young, colorful but clean, and very modern.

Target Market(s)

woman, 15-35

Industry/Entity Type

Cosmetics

Contact Information for Business Card

Full Name, address, phone

Font styles to use
Other font styles liked:
• Advent Pro

Colors
e34297
86cfc6
ffffff
5c5c5c
e8e8e8
e667a6
b2b2b2

Requirements
Must have
• One full colored side with a creative design and another with card info
• Use Color palette: #95C5C5 and/or #D38AA5
• Use fonts: Advent Pro
• Use website identity: https://www.glowmi-example.com
Nice to have
• If needed extra font: Roboto

```html
<!DOCTYPE html>
<html lang="en">
<head>
<meta charset="utf-8">
<title>Glowmi Business Card</title>
<link href="https://fonts.googleapis.com/css2?family=Advent+Pro:wght@300&family=Open+Sans:wght@400;600&display=swap" rel="stylesheet">
<style>
  :root {
    --backdrop: #2f2f2f;
    --teal: #7fc8c8;
    --teal-soft: #8fd0d0;
    --paper: #ffffff;
    --ink: #2a2a2a;
  }
  html, body {
    margin: 0;
    padding: 0;
    width: 1200px;
    height: 900px;
    overflow: hidden;
    background: var(--backdrop);
  }
  .stage {
    position: relative;
    width: 1200px;
    height: 900px;
  }
  .card {
    position: absolute;
    top: 306px;
    width: 440px;
    height: 271px;
    border-radius: 10px;
    overflow: hidden;
  }
  .card--front { left: 149px; background: var(--paper); }
  .card--back { left: 608px; background: var(--teal); }

  .front-band {
    position: absolute;
    left: 362px;
    top: 0;
    width: 78px;
    height: 100%;
    background: var(--teal);
  }
  .front-badge {
    position: absolute;
    left: 312px;
    top: 75px;
  }
  .wordmark {
    font-family: "Advent Pro", sans-serif;
    font-weight: 300;
    text-transform: uppercase;
    margin: 0;
    line-height: 1;
  }
  .front-wordmark {
    position: absolute;
    left: 21px;
    top: 32px;
    font-size: 52px;
    letter-spacing: 9px;
    color: var(--teal);
  }
  .contact {
    position: absolute;
    left: 23px;
    top: 126px;
    font-family: "Open Sans", sans-serif;
    color: var(--ink);
    font-size: 12px;
  }
  .contact-name {
    margin: 0;
    font-size: 14px;
    font-weight: 600;
    color: var(--teal);
    letter-spacing: 0.2px;
    line-height: 16px;
  }
  .contact-role { margin: 0 0 10px; line-height: 15px; }
  .contact-list { list-style: none; margin: 0 0 8px; padding: 0; }
  .contact-list li {
    display: flex;
    align-items: center;
    gap: 6px;
    line-height: 16px;
  }
  .contact-list svg { width: 9px; height: 9px; fill: var(--teal); flex: none; }
  .contact-address { margin: 0; line-height: 16px; }

  .back-texture {
    position: absolute;
    inset: 0;
    background: linear-gradient(135deg, var(--teal-soft), var(--teal));
  }
  .back-lockup {
    position: absolute;
    left: 70px;
    top: 100px;
    display: flex;
    align-items: center;
    gap: 26px;
  }
  .back-wordmark {
    font-size: 50px;
    letter-spacing: 6px;
    color: var(--paper);
  }
</style>
</head>
<body>
<main class="stage">
  <section class="card card--front" aria-label="Card front">
    <div class="front-band"></div>
    <svg class="front-badge" width="124" height="124" viewBox="0 0 124 124" aria-hidden="true">
      <circle cx="62" cy="62" r="62" fill="#ffffff"/>
      <circle cx="56" cy="62" r="47" fill="none" stroke="#7fc8c8" stroke-width="3"/>
    </svg>
    <h1 class="wordmark front-wordmark">Glowmi</h1>
    <div class="contact">
      <p class="contact-name">DANIEL REYES</p>
      <p class="contact-role">Managing Director</p>
      <ul class="contact-list">
        <li><svg viewBox="0 0 10 10"><path d="M2 0.5 L3.6 2.8 L2.8 3.8 Q4 6.2 6.2 7.2 L7.2 6.4 L9.5 8 L8.4 9.5 Q2.5 9 0.5 1.6 Z"/></svg>(044)555018273</li>
        <li><svg viewBox="0 0 10 10"><path d="M0 2 H10 V8 H0 Z M0.6 2.4 L5 5.6 L9.4 2.4" /></svg>hello@glowmi-example.com</li>
        <li><svg viewBox="0 0 10 10"><circle cx="5" cy="5" r="4.5"/></svg>www.glowmi-example.com</li>
      </ul>
      <p class="contact-address">1234, Address GoesHere,<br>Country name, 12345</p>
    </div>
  </section>

  <section class="card card--back" aria-label="Card back">
    <div class="back-texture" role="img" aria-label="Faint repeating brand-mark pattern in soft teal"></div>
    <div class="back-lockup">
      <svg width="74" height="74" viewBox="0 0 74 74" aria-hidden="true">
        <circle cx="37" cy="37" r="35" fill="none" stroke="#ffffff" stroke-width="3"/>
      </svg>
      <p class="wordmark back-wordmark">Glowmi</p>
    </div>
  </section>
</main>
</body>
</html>
```